I need a new business card design for my pharmacy.

I need a business card design. I will include my logo.
The card needs to be readable. I prefer to have my logo on one side along with my website, the other side includes the other information. Please use combination of black, neon green, white, and silver. This needs to catch the eye but yet be clearly visible and legible. Thanks

Industry/Entity Type

Pharmacy

Contact Information for Business Card

It needs to have the following information listed:
Mel's Apothecary Owner/Pharm D.
7134 North Brook Lane
Sioux Falls, SD 57231
Phone 605-318-6207
Fax 605-318-6209
email: mel@melsapothecary-example.com
www.melsapothecary-example.com
Store hours Monday-Friday 8 am- 7 pm
Saturday 8 am- 12 pm
Sunday Closed
Please utilize the colors black, white, and neon green, maybe silver.

Requirements
Must have
• It needs to be easily readable!
Nice to have
• It should catch the eye.
Should not have
• Do not use any other colors except listed: black, neon green, white, & silver.

```html
<!DOCTYPE html>
<html lang="en">
<head>
<meta charset="utf-8">
<title>Mel's Apothecary — Business Card</title>
<link href="https://fonts.googleapis.com/css2?family=Oswald:wght@300;400;500;600&display=swap" rel="stylesheet">
<style>
  :root {
    --bg: #d9d9d9;
    --card-black: #1c1c1c;
    --card-white: #ffffff;
    --neon: #4de83a;
    --silver: #b5b5b5;
    --ink: #2a2a2a;
    --label: #3a3a3a;
  }
  * { margin: 0; padding: 0; box-sizing: border-box; }
  html, body {
    width: 1200px; height: 1001px; overflow: hidden;
    background: var(--bg);
    font-family: "Oswald", "Arial Narrow", sans-serif;
  }
  .canvas { position: relative; width: 1200px; height: 1001px; }

  .card {
    position: absolute;
    width: 560px; height: 320px;
    box-shadow: 0 6px 18px rgba(0,0,0,0.18);
  }

  /* Front */
  .card-front {
    left: 90px; top: 110px;
    background: var(--card-black);
    color: var(--card-white);
  }
  .brand {
    position: absolute; right: 44px; top: 130px;
    text-align: right;
  }
  .brand-row { display: flex; align-items: center; justify-content: flex-end; gap: 12px; }
  .brand-dot { width: 18px; height: 18px; border-radius: 50%; background: var(--silver); }
  .brand-name {
    font-weight: 600; font-size: 38px; letter-spacing: 0.5px; line-height: 1;
    color: var(--card-white);
  }
  .brand-web {
    margin-top: 10px; font-weight: 300; font-size: 15px; letter-spacing: 0.8px;
    color: var(--card-white);
  }

  /* Back */
  .card-back {
    left: 560px; top: 540px;
    background: var(--card-white);
    color: var(--ink);
  }
  .contact {
    position: absolute; left: 280px; top: 26px; width: 260px;
  }
  .contact-item { margin-bottom: 6px; }
  .contact-label { font-weight: 300; font-size: 14px; color: var(--label); line-height: 1.15; }
  .contact-value { font-weight: 400; font-size: 17px; color: var(--neon); line-height: 1.15; white-space: nowrap; }
  .contact-value.small { font-size: 15px; }

  .owner {
    position: absolute; left: 28px; top: 196px;
  }
  .owner-role { font-weight: 300; font-size: 16px; color: var(--silver); letter-spacing: 0.5px; line-height: 1.1; }
  .owner-name { font-weight: 600; font-size: 20px; color: var(--neon); letter-spacing: 0.5px; line-height: 1.1; }

  .divider {
    position: absolute; left: 28px; right: 28px; top: 252px;
    height: 1px; background: var(--neon);
  }

  .hours {
    position: absolute; left: 28px; right: 20px; top: 266px;
    display: flex; align-items: baseline; gap: 10px; white-space: nowrap;
  }
  .hours-title { font-weight: 400; font-size: 12px; color: var(--neon); }
  .hours-text { font-weight: 300; font-size: 11px; letter-spacing: 3.2px; color: var(--ink); }
  .hours-sep { color: var(--neon); font-size: 12px; }
  .hours-closed { font-weight: 400; font-size: 11px; color: var(--neon); }
</style>
</head>
<body>
<div class="canvas">

  <section class="card card-front" aria-label="Card front">
    <div class="brand">
      <div class="brand-row">
        <span class="brand-dot"></span>
        <span class="brand-name">Mel's Apothecary</span>
      </div>
      <div class="brand-web">www.melsapothecary-example.com</div>
    </div>
  </section>

  <section class="card card-back" aria-label="Card back">
    <div class="contact">
      <div class="contact-item">
        <div class="contact-label">Phone :-</div>
        <div class="contact-value">605-318-6207</div>
      </div>
      <div class="contact-item">
        <div class="contact-label">Fax :-</div>
        <div class="contact-value">605-318-6209</div>
      </div>
      <div class="contact-item">
        <div class="contact-label">E-mail :-</div>
        <div class="contact-value small">mel@melsapothecary-example.com</div>
      </div>
      <div class="contact-item">
        <div class="contact-label">Address :-</div>
        <div class="contact-value small">7134 North Brook Lane Sioux Falls, SD 57231</div>
      </div>
    </div>

    <div class="owner">
      <div class="owner-role">OWNER/PHARM.D</div>
      <div class="owner-name">MEL'S APOTHECARY</div>
    </div>

    <div class="divider"></div>

    <div class="hours">
      <span class="hours-title">STORE HOURS</span>
      <span class="hours-text">MONDAY-FRIDAY 8AM-7PM</span>
      <span class="hours-sep">|</span>
      <span class="hours-text">SATURDAY 8AM-12PM</span>
      <span class="hours-closed">SUNDAY CLOSED</span>
    </div>
  </section>

</div>
</body>
</html>
```